Need a graphic design for front page of tech blog

Hi,

So I'm looking to start a project of redesigning the front homepage for all of my tech sites. I already have a developer that will code the change, so what I need from someone here is to give me a graphic design, which I can then give to my developers to code.

Currently, I have the plain old boring default list of PressLeaf posts as the front page, which needs to be replaced with something a little more like a magazine or newspaper style. You can see my four sites here:

https://www.quill-gadget-notes.com/
https://servicebenchnerd.com/
https://theatticbitworks.com/
https://www.hoppingtolark.com/

I've attached some screenshots of mobile sites that I like in terms of look and style. Some desktop sites that I like are here (I like some parts more than others, I've attached screenshots of the sections I like):

https://www.ploddernook.com/
https://www.gizmonest.com/
https://www.pinewirebulletin.com/
https://www.takeholdwith.com/
https://www.dayspool.com/

Basically, I don't need all that text after each post. Seems like most sites now just have an image, a title, the author and date info and possibly the category.

Right now I'm only showing 10 posts and one has to scroll through lots of text to see them all. The sidebar is good, but I think we can get rid of that for the front page and instead have different sections like Latest Tips, and then some section headers based on the categories.

Anyway, I'm looking for someone who can come up with multiple designs, so that I have some choice.

I'm looking to get this done over the next few weeks. Also, please include in your price the cost of any revisions and how many revisions can be done.

Thanks

Tarun

```html
<!DOCTYPE html>
<html lang="en">
<head>
<meta charset="utf-8">
<title>ServiceBenchNerd – Front Page</title>
<link href="https://fonts.googleapis.com/css2?family=Crimson+Text:ital,wght@0,400;0,600;1,400&display=swap" rel="stylesheet">
<style>
:root{
  --ink:#222;
  --muted:#555;
  --link:#3b6db3;
  --accent:#2f7bd6;
  --head-top:#2b2f36;
  --head-bottom:#15181c;
  --line:#e3e3e3;
  --foot:#1a1d22;
  --foot-bar:#121418;
  --white:#fff;
}
*{box-sizing:border-box;margin:0;padding:0}
html,body{width:867px;height:1200px;overflow:hidden}
body{position:relative;background:var(--white);font-family:"Crimson Text",Georgia,serif;color:var(--ink)}
a{color:var(--link)}

/* masthead */
.masthead{position:absolute;left:0;top:0;width:867px;height:54px;background:linear-gradient(var(--head-top),var(--head-bottom));border-bottom:2px solid var(--accent)}
.brand-mark{position:absolute;left:163px;top:3px;width:42px;height:42px;border-radius:50%;background:radial-gradient(circle at 40% 35%,#4a9af0,#1d5fb8);border:2px solid #dfe8f3;z-index:3}
.brand-name{position:absolute;left:213px;top:4px;color:var(--white);font-size:15px;letter-spacing:1px;font-weight:400}
.main-nav{position:absolute;left:210px;top:34px;display:flex;gap:12px;list-style:none}
.main-nav li{color:var(--white);font-size:6.8px;letter-spacing:.6px;padding:2px 4px}
.main-nav li.active{border-bottom:1px solid #9ab}
.social{position:absolute;left:616px;top:9px;display:flex;gap:7px}
.social span{width:10px;height:10px;border-radius:50%;background:#e8e8e8}
.social span.on{background:var(--accent)}
.search{position:absolute;left:619px;top:34px;display:flex}
.search .field{width:73px;height:11px;background:var(--white);font-size:6px;font-style:italic;color:#888;padding:1px 3px}
.search .go{width:11px;height:11px;background:#8a8f96;border-left:1px solid #555}

.dropdown{position:absolute;left:210px;top:54px;width:93px;height:92px;background:rgba(24,27,32,.96);list-style:none;padding-top:4px;z-index:5}
.dropdown li{color:var(--white);font-size:7px;letter-spacing:.4px;height:14.7px;line-height:14.7px;padding-left:4px}
.dropdown li.current{color:var(--accent)}

/* posts */
.posts{position:absolute;left:162px;top:90px;display:grid;grid-template-columns:173px 173px;grid-auto-rows:62px;column-gap:13px;row-gap:12.8px}
.card{display:flex;border:1px solid var(--line);box-shadow:0 1px 2px rgba(0,0,0,.07);background:var(--white)}
.thumb{width:86px;flex:none;height:100%}
.info{padding:4px 4px 0 4px;font-size:6.3px;line-height:1.33}
.info h2{font-size:6.3px;font-weight:600;color:var(--ink);margin-bottom:2px}
.info p{color:var(--muted)}
.info p.spacer{margin-top:14px}

/* sidebar */
.newsletter{position:absolute;left:532px;top:90px;width:172px;height:46px;border:1px solid var(--line);border-top:2px solid #c9d6e6;text-align:center}
.newsletter h3{font-size:7px;font-weight:400;letter-spacing:.6px;font-variant:small-caps;margin-top:7px}
.newsletter .field{margin:4px auto 0;width:148px;height:11px;border:1px solid #bbb;font-size:6px;font-style:italic;color:#888;text-align:left;padding:1px 3px;position:relative}
.newsletter .field::after{content:"";position:absolute;right:0;top:0;width:8px;height:9px;background:var(--accent)}
.side-section{position:absolute;left:532px;width:172px}
.side-section h3{font-size:7px;font-style:italic;font-weight:400;color:var(--link);letter-spacing:.4px;border-bottom:1px solid var(--line);padding-bottom:2px;margin-bottom:10px}
.tiles{display:grid;grid-template-columns:86px 86px;grid-auto-rows:94px}
.tile{text-align:center}
.tile .pic{width:72px;height:56px;margin:0 auto}
.tile p{font-size:5.6px;font-variant:small-caps;letter-spacing:.3px;line-height:1.35;margin-top:4px;padding:0 2px}

/* footer */
.site-footer{position:absolute;left:0;top:1040px;width:867px;height:160px;background:var(--foot);border-top:2px solid var(--accent);color:#e6e6e6}
.deco-left{position:absolute;left:0;top:0;width:170px;height:112px;background:linear-gradient(135deg,#2f3a4d,#161a20 70%)}
.deco-right{position:absolute;right:0;top:20px;width:160px;height:92px;background:linear-gradient(225deg,#1f5c6b,#3a2c5a 45%,#161a20 85%)}
.footer-mark{position:absolute;left:413px;top:-23px;width:42px;height:42px;border-radius:50%;background:radial-gradient(circle at 40% 35%,#4a9af0,#1d5fb8);border:2px solid #dfe8f3}
.fcol{position:absolute;top:32px;font-size:6.5px;line-height:1.4}
.fcol h4{font-size:7px;font-weight:400;letter-spacing:.6px;margin-bottom:7px}
.fcol.family{left:171px;width:140px}
.fcol.family ul{list-style:none;margin-top:8px}
.fcol.family li{text-decoration:underline}
.fcol.family li::before{content:"• "}
.fcol.family li.current{color:var(--accent)}
.fcol.signup{left:357px;width:153px;text-align:center}
.fcol.signup .field{height:12px;background:var(--white);color:#888;font-style:italic;text-align:left;padding:1px 4px;position:relative}
.fcol.signup .field::after{content:"";position:absolute;right:1px;top:1px;width:7px;height:10px;background:var(--accent)}
.fcol.signup .social{position:static;justify-content:center;margin-top:17px}
.fcol.about{left:533px;width:162px;font-size:6.1px;line-height:1.3}
.fcol.about .more{text-align:right;text-decoration:underline;margin-top:6px}
.footer-bar{position:absolute;left:0;top:110px;width:867px;height:50px;background:var(--foot-bar);text-align:center;font-size:6.3px}
.footer-bar ul{display:flex;justify-content:center;gap:18px;list-style:none;margin-top:8px}
.footer-bar p{margin-top:6px}
</style>
</head>
<body>

<header class="masthead">
  <div class="brand-mark"></div>
  <div class="brand-name">SERVICEBENCHNERD</div>
  <ul class="main-nav">
    <li class="active">PANES</li>
    <li>TIPS ▴</li>
    <li>SOFTWARE ▴</li>
    <li>OTHER ▴</li>
  </ul>
  <div class="social"><span></span><span class="on"></span><span></span><span></span><span></span></div>
  <div class="search"><div class="field">search</div><div class="go"></div></div>
</header>

<ul class="dropdown">
  <li>COMPUTER TIPS</li>
  <li class="current">SEARCHLY TIPS</li>
  <li>WEBROAMER</li>
  <li>OFFICESUITE TIPS</li>
  <li>ORCHARD OS</li>
  <li>WEB SITE TIPS</li>
</ul>

<main class="posts">
  <article class="card"><div class="thumb" role="img" aria-label="Padlock on a green and dark background" style="background:linear-gradient(90deg,#3aa63a,#2a2e33)"></div><div class="info"><h2>How To Change Your PressLeaf Login Page URL For Better Security</h2><p>March 1st, 2019</p><p>by <a>Nolan Price</a></p><p>File in: <a>Web Site Tips</a></p></div></article>
  <article class="card"><div class="thumb" role="img" aria-label="Dark mode browser settings screen" style="background:linear-gradient(#2a3242,#1a2230)"></div><div class="info"><h2>How to Enable Dark Mode Everywhere on Panes 10</h2><p>February 28th, 2019</p><p>by <a>Remy Holt</a></p><p>File in: <a>Panes 10</a></p></div></article>

  <article class="card"><div class="thumb" role="img" aria-label="Colourful chart graphic" style="background:linear-gradient(135deg,#e9f6f8,#f6dcd3)"></div><div class="info"><h2>Make a Web App Run Like a Desktop App</h2><p>February 27th, 2019</p><p>by <a>Owen Barrow</a></p><p>File in: <a>How-To</a></p></div></article>
  <article class="card"><div class="thumb" role="img" aria-label="Start menu screenshot" style="background:linear-gradient(#3a3d42,#e6e6e6 85%)"></div><div class="info"><h2>What to Do If Your Panes 10 Start Menu Doesn't Work?</h2><p>February 26th, 2019</p><p>by <a>Lucas Ray Moreno</a></p><p>File in: <a>Panes 10</a></p></div></article>

  <article class="card"><div class="thumb" role="img" aria-label="Blue warning screen" style="background:linear-gradient(135deg,#2f6fc0,#1b4a8a)"></div><div class="info"><h2>7 Ways to Clear Memory and Boost RAM on Panes</h2><p>February 25th, 2019</p><p>by <a>Nolan Price</a></p><p>File in: <a>How-To</a></p></div></article>
  <article class="card"><div class="thumb" role="img" aria-label="Web address with a cursor" style="background:linear-gradient(135deg,#f2f4f7,#a9c4e8)"></div><div class="info"><h2>Find a Domain's Backlinks, Redirects, and Shared IPs</h2><p>February 22nd, 2019</p><p>by <a>Kurt Lindell</a></p><p>File in: <a>How-To</a></p></div></article>

  <article class="card"><div class="thumb" role="img" aria-label="Command line window" style="background:#111"></div><div class="info"><h2>21 CMD Commands All Panes Users Should Know</h2><p>February 21st, 2019</p><p>by <a>Nolan Price</a></p><p>File in: <a>Help Desk</a></p></div></article>
  <article class="card"><div class="thumb" role="img" aria-label="Run dialog box" style="background:linear-gradient(#dfe9df 15%,#f7f7f7 15%)"></div><div class="info"><h2>Use This Script to Rename Multiple Files at Once in Panes</h2><p>February 20th, 2019</p><p>by <a>Tarun Mehra</a></p><p>File in: <a>How-To</a></p></div></article>

  <article class="card"><div class="thumb" role="img" aria-label="Hard drive wrapped in a chain and padlock" style="background:linear-gradient(135deg,#e8e8e8,#6d6f73)"></div><div class="info"><h2>How To Set Up Full Disk Encryption On Panes With VaultLock</h2><p>February 19th, 2019</p><p>by <a>Dale Morrow</a></p><p>File in: <a>Panes 10</a></p></div></article>
  <article class="card"><div class="thumb" role="img" aria-label="Settings search result screenshot" style="background:linear-gradient(#f4f4f4,#dfe7f2)"></div><div class="info"><h2>How to Block Access to Panes 10 Settings and Control Panel</h2><p>February 18th, 2019</p><p>by <a>Remy Holt</a></p><p>File in: <a>Panes 10</a></p></div></article>

  <article class="card"><div class="thumb" role="img" aria-label="Breach check website screenshot" style="background:linear-gradient(#1f2328 15%,#1f6d8e 15%)"></div><div class="info"><h2>Find Out If Your Email Has Been Compromised in a Data Breach</h2><p>February 14th, 2019</p><p>by <a>Simon Keele</a></p><p>File in: <a>How-To</a></p></div></article>
  <article class="card"><div class="thumb" role="img" aria-label="News portal on a laptop screen" style="background:linear-gradient(135deg,#2f7de0,#e9eef5)"></div><div class="info"><p class="spacer">February 28th, 2019</p><p>by <a>Remy Holt</a></p><p>File in: <a>Panes 10</a></p></div></article>

  <article class="card"><div class="thumb" role="img" aria-label="Context menu with command prompt options" style="background:linear-gradient(#2a2d31,#15171a)"></div><div class="info"><h2>Replace Command Prompt with ShellPlus and Vice Versa in Panes 10</h2><p>February 12th, 2019</p><p>by <a>Tarun Mehra</a></p><p>File in: <a>Panes 10</a></p></div></article>
  <article class="card"><div class="thumb" role="img" aria-label="Diagnostic tools illustration" style="background:linear-gradient(135deg,#cfe6f7,#3f9ad6)"></div><div class="info"><h2>15 Panes Diagnostics Tools to Improve Your PC's Health</h2><p>February 11th, 2019</p><p>by <a>Nolan Price</a></p><p>File in: <a>Tools Review</a></p></div></article>

  <article class="card"><div class="thumb" role="img" aria-label="Binary digits under a magnifying glass" style="background:linear-gradient(135deg,#1a8fd8,#0b3d72)"></div><div class="info"><p class="spacer">February 8th, 2019</p><p>by <a>Nolan Price</a></p><p>File in: <a>Networking</a></p></div></article>
  <article class="card"><div class="thumb" role="img" aria-label="Blue glowing website emblem" style="background:radial-gradient(circle,#2a7ab8,#0b2240)"></div><div class="info"><h2>How To Make It Harder For Someone To Hack Into Your PressLeaf Site</h2><p>February 7th, 2019</p><p>by <a>Dale Morrow</a></p><p>File in: <a>Panes 10</a></p></div></article>

  <article class="card"><div class="thumb" role="img" aria-label="Search engine home page" style="background:linear-gradient(135deg,#ffffff,#d9dde3)"></div><div class="info"><h2>Advanced Searchly Searching Using Search Operators</h2><p>February 6th, 2019</p><p>by <a>Kurt Lindell</a></p><p>File in: <a>How-To</a></p></div></article>
  <article class="card"><div class="thumb" role="img" aria-label="Hooded figure in the dark" style="background:radial-gradient(circle,#24384a,#0a1118)"></div><div class="info"><h2>4 Great Anonymous and Private Email Services</h2><p>February 5th, 2019</p><p>by <a>Tarun Mehra</a></p><p>File in: <a>Tools Review</a></p></div></article>

  <article class="card"><div class="thumb" role="img" aria-label="Spreadsheet of numbers" style="background:linear-gradient(135deg,#e6f0f8,#9cbad6)"></div><div class="info"><h2>How to Create a Simple Pivot Table in Gridsheet</h2><p>February 4th, 2019</p><p>by <a>Tarun Mehra</a></p><p>File in: <a>Office Tips</a></p></div></article>
  <article class="card"><div class="thumb" role="img" aria-label="Night landscape wallpaper" style="background:linear-gradient(#2a2f2a,#6b4a22)"></div><div class="info"><h2>Amazing Live Wallpapers for Panes 10 to Transform Your Desktop</h2><p>February 1st, 2019</p><p>by <a>Nolan Price</a></p><p>File in: <a>Panes 10</a></p></div></article>

  <article class="card"><div class="thumb" role="img" aria-label="Speedometer gauge" style="background:radial-gradient(circle at 70% 70%,#b22,#e8e2dc 60%)"></div><div class="info"><h2>How to Overclock a Corex Processor (CPU)</h2><p>January 31st, 2019</p><p>by <a>Remy Holt</a></p><p>File in: <a>How-To</a></p></div></article>
  <article class="card"><div class="thumb" role="img" aria-label="Red warning graphic" style="background:linear-gradient(#e0323a,#b51c24)"></div><div class="info"><h2>Why You Shouldn't Download SweepKit for Panes Anymore</h2><p>January 30th, 2019</p><p>by <a>Nolan Price</a></p><p>File in: <a>Tools Review</a></p></div></article>

  <article class="card"><div class="thumb" role="img" aria-label="Team chat illustration" style="background:linear-gradient(135deg,#8fd3de,#3aa8b8)"></div><div class="info"><h2>Best Free Team Chat Software for Panes 10</h2><p>January 29th, 2019</p><p>by <a>Remy Holt</a></p><p>File in: <a>Tools Review</a></p></div></article>
  <article class="card"><div class="thumb" role="img" aria-label="Microphone with headphones" style="background:radial-gradient(circle at 70% 40%,#8ac43a,#1c1e1c 60%)"></div><div class="info"><h2>How to Fix a Microphone Not Working on Panes 10</h2><p>January 28th, 2019</p><p>by <a>Remy Holt</a></p><p>File in: <a>Panes 10</a></p></div></article>
</main>

<aside>
  <div class="newsletter"><h3>Daily Email Newsletter</h3><div class="field">Enter your email and hit enter</div></div>

  <section class="side-section" style="top:149px"><h3>LATEST REVIEWS</h3><div class="tiles">
    <div class="tile"><div class="pic" role="img" aria-label="Diagnostic tools illustration" style="background:linear-gradient(135deg,#cfe6f7,#3f9ad6)"></div><p>15 Panes Diagnostics Tools to Improve Your PC's Health</p></div>
    <div class="tile"><div class="pic" role="img" aria-label="Hooded figure in the dark" style="background:radial-gradient(circle,#24384a,#0a1118)"></div><p>4 Great Anonymous and Private Email Services</p></div>
    <div class="tile"><div class="pic" role="img" aria-label="Red warning graphic" style="background:linear-gradient(#e0323a,#b51c24)"></div><p>Why You Shouldn't Download SweepKit for Panes Anymore</p></div>
    <div class="tile"><div class="pic" role="img" aria-label="Team chat illustration" style="background:linear-gradient(135deg,#8fd3de,#3aa8b8)"></div><p>Best Free Team Chat Software for Panes 10</p></div>
  </div></section>

  <section class="side-section" style="top:369px"><h3>LATEST TIPS</h3><div class="tiles">
    <div class="tile"><div class="pic" role="img" aria-label="Security icon on dark tile" style="background:#2c3138"></div><p>How to Change Your PressLeaf Login Page URL for Better Security</p></div>
    <div class="tile"><div class="pic" role="img" aria-label="Colourful chart graphic" style="background:linear-gradient(135deg,#fff,#f6cfc0)"></div><p>Make a Web App Run Like a Desktop App</p></div>
    <div class="tile"><div class="pic" role="img" aria-label="Blue warning screen" style="background:linear-gradient(135deg,#2f6fc0,#1b4a8a)"></div><p>7 Ways to Clear Memory and Boost RAM on Panes</p></div>
    <div class="tile"><div class="pic" role="img" aria-label="Web address with a cursor" style="background:linear-gradient(135deg,#f2f4f7,#a9c4e8)"></div><p>Find a Domain's Backlinks, Redirects, and Shared IPs</p></div>
  </div></section>

  <section class="side-section" style="top:589px"><h3>OS NEWS</h3><div class="tiles">
    <div class="tile"><div class="pic" role="img" aria-label="Dark mode file explorer" style="background:#121212"></div><p>How to Enable Dark Mode Everywhere on Panes 10</p></div>
    <div class="tile"><div class="pic" role="img" aria-label="Start menu screenshot" style="background:linear-gradient(#3a3d42,#e6e6e6 85%)"></div><p>What to Do If Your Panes 10 Start Menu Doesn't Work?</p></div>
    <div class="tile"><div class="pic" role="img" aria-label="Hard drive wrapped in a chain and padlock" style="background:linear-gradient(135deg,#f0f0f0,#6d6f73)"></div><p>How To Set Up Full Disk Encryption on Panes With VaultLock</p></div>
    <div class="tile"><div class="pic" role="img" aria-label="Settings search result screenshot" style="background:linear-gradient(90deg,#1c1c1c 25%,#eef2f8 25%)"></div><p>How to Block Access to Panes 10 Settings and Control Panel</p></div>
  </div></section>

  <section class="side-section" style="top:808px"><h3>OTHER NEWS</h3><div class="tiles">
    <div class="tile"><div class="pic" role="img" aria-label="Binary digits under a magnifying glass" style="background:linear-gradient(135deg,#1a8fd8,#0b3d72)"></div><p></p></div>
    <div class="tile"><div class="pic" role="img" aria-label="Network cable plugs" style="background:linear-gradient(135deg,#fafafa,#bcc6d0)"></div><p>WiFi Extenders vs Powerline Adapters – Which is the Best?</p></div>
    <div class="tile"><div class="pic" role="img" aria-label="Network switch device" style="background:linear-gradient(#fff,#2a2c30 55%)"></div><p>Router vs Switch vs Hub vs Modem vs Access Point vs Gateway</p></div>
    <div class="tile"><div class="pic" role="img" aria-label="Server setup wizard screenshot" style="background:linear-gradient(#f7f7f7,#e3e3e3)"></div><p>How to Create an FTP Server Using FileRaptor</p></div>
  </div></section>
</aside>

<footer class="site-footer">
  <div class="deco-left" role="img" aria-label="Keyboard close-up in blue light"></div>
  <div class="deco-right" role="img" aria-label="Backlit keyboard in rainbow light"></div>
  <div class="footer-mark"></div>

  <div class="fcol family">
    <h4>OUR PUBLISHING FAMILY</h4>
    <p>Quill Gadget Notes is part of the KV Internet Consulting publishing family.</p>
    <ul><li>SERVICE BENCH NERD</li><li class="current">THE ATTIC BITWORKS</li><li>HOPPING TO LARK</li></ul>
  </div>

  <div class="fcol signup">
    <h4>DAILY EMAIL NEWSLETTER</h4>
    <div class="field">Enter your email and hit enter</div>
    <div class="social"><span></span><span></span><span></span><span class="on"></span><span></span></div>
  </div>

  <div class="fcol about">
    <h4 style="text-align:center">ABOUT QUILL GADGET NOTES</h4>
    <p>Welcome to Quill Gadget Notes – A blog that provide readers with daily computer tutorials, technology news, software reviews, and personal computing tips. My name is Tarun Mehra and I am a full-time professional blogger. I graduated from Alder University with a degree in Computer Science and Mathematics.</p>
    <p class="more">Read More</p>
  </div>

  <div class="footer-bar">
    <ul><li>Home</li><li>About</li><li>Contact</li><li>Privacy Policy</li></ul>
    <p>Copyright © 2007-2019 Quill Gadget Notes.com, LLC All Rights Reserved</p>
  </div>
</footer>

</body>
</html>
```